CareVantRx business cards

We need a business card design that we could customize as needed for employees. We will need space for Name, Title, 1-2 phone numbers and email address.

We are a Pharmacy Benefits Management (PBM) company for hospice agencies and beginning a nationwide expansion. Attached is a vector file of our logo.

Cards can be single or double sided.

Industry/Entity Type

Business

```html
<!DOCTYPE html>
<html lang="en">
<head>
<meta charset="utf-8">
<title>CareVantRx Business Cards</title>
<link rel="stylesheet" href="https://fonts.googleapis.com/css2?family=Arimo:wght@400;700&display=swap">
<style>
  :root {
    --backdrop: #e9ebec;
    --card-white: #ffffff;
    --brand-blue: #336a8e;
    --brand-green: #7f9f4e;
    --ink: #2b2b2b;
  }
  * { margin: 0; padding: 0; box-sizing: border-box; }
  html, body {
    width: 1200px; height: 900px; overflow: hidden;
    background: var(--backdrop);
    font-family: "Arimo", Arial, sans-serif;
  }
  .card {
    position: absolute;
    left: 280px;
    width: 640px; height: 366px;
    border-radius: 30px;
    overflow: hidden;
    box-shadow: 0 6px 18px rgba(0,0,0,0.18);
  }
  .card-back { top: 46px; background: var(--brand-blue); }
  .card-front { top: 484px; background: var(--card-white); }
  .card svg.band { position: absolute; left: 0; bottom: 0; width: 640px; height: 366px; }

  .brand {
    position: absolute;
    display: flex; align-items: center; gap: 14px;
    font-weight: 400; letter-spacing: -0.5px;
  }
  .brand-square { width: 52px; height: 52px; border-radius: 6px; }
  .card-back .brand { left: 50%; top: 142px; transform: translateX(-50%); color: var(--brand-green); font-size: 56px; }
  .card-back .brand-square { background: var(--brand-green); }
  .card-front .brand { left: 50%; top: 122px; transform: translateX(-50%); color: var(--brand-green); font-size: 60px; }
  .card-front .brand-square { background: var(--brand-blue); }

  .person { position: absolute; left: 112px; top: 272px; text-align: right; }
  .person-name { color: var(--brand-green); font-weight: 700; font-size: 19px; letter-spacing: 0.3px; }
  .person-title { color: var(--ink); font-size: 16px; margin-top: 2px; }

  .contact { position: absolute; left: 350px; top: 276px; color: var(--ink); font-size: 15px; line-height: 22px; }
  .contact-row { display: flex; align-items: center; gap: 10px; }
  .contact-row svg { width: 13px; height: 13px; fill: var(--brand-green); flex: none; }
</style>
</head>
<body>

<section class="card card-back" aria-label="Card back">
  <svg class="band" viewBox="0 0 640 366" aria-hidden="true">
    <path d="M640 300 C600 300 560 318 520 336 L455 366 L640 366 Z" fill="var(--brand-green)"/>
  </svg>
  <div class="brand"><span class="brand-square"></span>CareVantRx</div>
</section>

<section class="card card-front" aria-label="Card front">
  <svg class="band" viewBox="0 0 640 366" aria-hidden="true">
    <path d="M0 344 C0 336 8 332 20 332 L470 332 C492 332 505 346 512 366 L0 366 Z" fill="var(--brand-blue)"/>
  </svg>
  <div class="brand"><span class="brand-square"></span>CareVantRx</div>

  <div class="person">
    <div class="person-name">DANIEL BROOKS</div>
    <div class="person-title">Occupation</div>
  </div>

  <div class="contact">
    <div class="contact-row">
      <svg viewBox="0 0 24 24"><path d="M6.6 10.8a15 15 0 0 0 6.6 6.6l2.2-2.2c.3-.3.7-.4 1-.2 1.1.4 2.3.6 3.6.6.6 0 1 .4 1 1V20c0 .6-.4 1-1 1A17 17 0 0 1 3 4c0-.6.4-1 1-1h3.5c.6 0 1 .4 1 1 0 1.3.2 2.5.6 3.6.1.3 0 .7-.2 1z"/></svg>
      <span>000-0000-000 / 000-0000-000</span>
    </div>
    <div class="contact-row">
      <svg viewBox="0 0 24 24"><path d="M2 5h20v14H2z M2 5l10 8 10-8" stroke="#fff" stroke-width="1.5"/></svg>
      <span>info@carevantrx.com</span>
    </div>
  </div>
</section>

</body>
</html>
```